Quavi Sales Pipeline

We need an infographic to help the sales team understand the importance of a sales pipeline and how to grow and manage it. It's important that they understand every process plays a vital part and a complete circle. If you break one part, the sales process can be a failure.

Target Market(s)

Infographic Designer

Font styles to use
Serif

Colors
33b8a4
abd037

Requirements
Must have
• Have fun!
Nice to have
• Open to all ideas. Keep in mind that we are eastern philosophy focused!
Should not have
• Not applicable! Just have phone

```html
<!DOCTYPE html>
<html lang="en">
<head>
<meta charset="utf-8">
<title>Quavi Sales Pipeline Lifecycle</title>
<link rel="stylesheet" href="https://fonts.googleapis.com/css2?family=Roboto:wght@500;700;900&display=swap">
<style>
  :root {
    --page-bg: #eef0f2;
    --sheet: #ffffff;
    --navy: #2b4a6b;
    --navy-deep: #1f3d5c;
    --ribbon-tail: #2f66a3;
    --footer-band: #4a7fb5;
    --label: #2d5c8a;
    --ring-top: #4f80ad;
    --ring-right: #5d91c6;
    --ring-br: #2b8ae0;
    --ring-bl: #24568f;
    --ring-left: #2e5a86;
    --center-num: #8fb3d9;
    --wash: #e6edf5;
  }
  * { margin: 0; padding: 0; box-sizing: border-box; }
  html, body { width: 1200px; height: 1200px; overflow: hidden; background: var(--page-bg); }
  body { position: relative; font-family: "Roboto", Arial, sans-serif; }

  .poster {
    position: absolute; left: 166px; top: 20px;
    width: 868px; height: 1160px;
    background: linear-gradient(180deg, var(--wash) 0%, var(--sheet) 14%, var(--sheet) 60%, var(--wash) 100%);
    overflow: hidden;
  }
  .brand {
    position: absolute; top: 46px; left: 0; width: 100%;
    display: flex; justify-content: center; align-items: center; gap: 14px;
  }
  .brand-dot { width: 44px; height: 44px; border-radius: 50%; background: var(--ring-br); }
  .brand-name { font-weight: 900; font-size: 56px; color: var(--navy-deep); line-height: 1; }

  .title-ribbon { position: absolute; left: 0; top: 0; width: 868px; height: 280px; }
  .title-text {
    position: absolute; top: 147px; left: 72px; width: 724px; height: 67px;
    display: flex; align-items: center; justify-content: center;
    color: #fff; font-weight: 900; font-size: 45px; letter-spacing: 0.5px;
  }

  .lifecycle { position: absolute; left: 0; top: 0; width: 868px; height: 1160px; }
  .stage-label { font-family: "Roboto", Arial, sans-serif; font-weight: 700; font-size: 17px; fill: var(--label); }
  .center-num { font-family: "Roboto", Arial, sans-serif; font-weight: 900; font-size: 88px; fill: var(--center-num); }
  .center-word { font-family: "Roboto", Arial, sans-serif; font-weight: 700; font-size: 30px; fill: #fff; }
  .icon { fill: none; stroke: var(--label); stroke-width: 2.6; stroke-linecap: round; stroke-linejoin: round; }

  .footer-band { position: absolute; left: 0; bottom: 0; width: 100%; height: 61px; background: var(--footer-band); }
  .site-pill {
    position: absolute; left: 259px; top: 1095px; width: 434px; height: 42px;
    background: var(--navy); border: 2px solid #fff; border-radius: 21px;
    display: flex; align-items: center; justify-content: center; gap: 18px;
    color: #fff; font-weight: 700; font-size: 25px;
  }
</style>
</head>
<body>
<main class="poster">
  <div class="brand">
    <span class="brand-dot"></span>
    <span class="brand-name">Quavi</span>
  </div>

  <svg class="title-ribbon" viewBox="0 0 868 280" aria-hidden="true">
    <polygon points="18,191 100,191 100,259 18,259 42,225" fill="var(--ribbon-tail)"/>
    <polygon points="850,191 768,191 768,259 850,259 826,225" fill="var(--ribbon-tail)"/>
    <polygon points="72,214 100,214 100,236" fill="#173350"/>
    <polygon points="796,214 768,214 768,236" fill="#173350"/>
    <rect x="72" y="147" width="724" height="67" fill="var(--navy)"/>
  </svg>
  <h1 class="title-text">SALES PIPELINE LIFECYCLE</h1>

  <svg class="lifecycle" viewBox="0 0 868 1160">
    <defs>
      <linearGradient id="band" x1="0" y1="0" x2="1" y2="1">
        <stop offset="0" stop-color="#2f5f8f"/>
        <stop offset="0.6" stop-color="#4f86bd"/>
        <stop offset="1" stop-color="#2b8ae0"/>
      </linearGradient>
    </defs>
    <!-- connecting band -->
    <polygon points="448,410 707,566 612,894 277,894 182,594" fill="none" stroke="url(#band)" stroke-width="72" stroke-linejoin="round"/>
    <line x1="448" y1="410" x2="448" y2="676" stroke="var(--ring-top)" stroke-width="60"/>
    <line x1="707" y1="566" x2="448" y2="676" stroke="var(--ring-right)" stroke-width="60"/>
    <line x1="612" y1="894" x2="448" y2="676" stroke="var(--ring-br)" stroke-width="60"/>
    <line x1="277" y1="894" x2="448" y2="676" stroke="var(--ring-bl)" stroke-width="60"/>
    <line x1="182" y1="594" x2="448" y2="676" stroke="var(--ring-left)" stroke-width="60"/>

    <!-- center -->
    <circle cx="448" cy="676" r="128" fill="#cfdbe6"/>
    <circle cx="448" cy="676" r="116" fill="var(--navy)"/>
    <text class="center-num" x="448" y="676" text-anchor="middle">5</text>
    <text class="center-word" x="448" y="714" text-anchor="middle">KEY</text>
    <text class="center-word" x="448" y="748" text-anchor="middle">FOCUSES</text>

    <!-- top: collection -->
    <g>
      <circle cx="448" cy="410" r="114" fill="#fff" stroke="var(--ring-top)" stroke-width="16"/>
      <path class="icon" d="M410 345 h30 l22 -8 h16 M440 345 v14 h40 M432 364 l4 10 M448 370 l4 10 M440 384 l4 10"/>
      <rect class="icon" x="410" y="398" width="76" height="10" rx="3"/>
      <text class="stage-label" x="448" y="450" text-anchor="middle">COLLECTION</text>
      <text class="stage-label" x="448" y="472" text-anchor="middle">/BUILD UP (SEED)</text>
    </g>
    <!-- right: nurture -->
    <g>
      <circle cx="707" cy="566" r="114" fill="#fff" stroke="var(--ring-right)" stroke-width="16"/>
      <path class="icon" d="M680 500 q-10 14 0 20 q10 -6 0 -20 z"/>
      <circle class="icon" cx="736" cy="508" r="9"/>
      <path class="icon" d="M736 490 v-5 M754 508 h5 M718 508 h-5 M736 526 v5 M707 560 v-22 q-16 -2 -18 -16 q14 0 18 14 q4 -14 18 -14 q-2 14 -18 16 M682 548 q0 20 20 24 M732 548 q0 20 -20 24"/>
      <text class="stage-label" x="707" y="592" text-anchor="middle">NURTURE /RAPPORT</text>
      <text class="stage-label" x="707" y="614" text-anchor="middle">(WATER &amp; SUN)</text>
    </g>
    <!-- bottom right: engagement -->
    <g>
      <circle cx="612" cy="894" r="114" fill="#fff" stroke="var(--ring-br)" stroke-width="16"/>
      <path class="icon" d="M586 818 l28 40 l16 -8 l-20 -40 z M600 850 l-10 40 M614 858 l6 36 M630 850 l20 18 l-6 8 l-22 -14"/>
      <text class="stage-label" x="612" y="924" text-anchor="middle">ENGAGEMENT</text>
      <text class="stage-label" x="612" y="946" text-anchor="middle">/HARVEST (PRUNE)</text>
    </g>
    <!-- bottom left: peak -->
    <g>
      <circle cx="277" cy="894" r="114" fill="#fff" stroke="var(--ring-bl)" stroke-width="16"/>
      <path class="icon" d="M244 826 q14 8 28 0 l-6 14 q18 14 18 34 q0 16 -26 16 q-26 0 -26 -16 q0 -20 18 -34 z M296 862 h22 l-4 28 h-14 z M307 862 v-20 q-12 -2 -12 -12 q12 0 12 12 q2 -14 14 -14 q0 12 -14 14"/>
      <text class="stage-label" x="277" y="914" text-anchor="middle">PEAK/SUMMIT</text>
      <text class="stage-label" x="277" y="936" text-anchor="middle">(PACKAGE/</text>
      <text class="stage-label" x="277" y="958" text-anchor="middle">PRESENTATION)</text>
    </g>
    <!-- left: retention -->
    <g>
      <circle cx="182" cy="594" r="114" fill="#fff" stroke="var(--ring-left)" stroke-width="16"/>
      <path class="icon" d="M156 560 a32 32 0 0 1 54 -30 M208 568 a32 32 0 0 1 -54 24"/>
      <circle class="icon" cx="213" cy="530" r="4"/>
      <path class="icon" d="M182 584 v-54 M182 570 q-14 -2 -14 -14 q14 0 14 14 q0 -14 14 -14 q0 12 -14 14 M182 552 q-10 -2 -10 -12 q10 0 10 12 q0 -12 10 -12 q0 10 -10 12"/>
      <text class="stage-label" x="182" y="622" text-anchor="middle">RETENTION</text>
      <text class="stage-label" x="182" y="644" text-anchor="middle">/DESCENT</text>
      <text class="stage-label" x="182" y="666" text-anchor="middle">(PLANT)</text>
    </g>
  </svg>

  <div class="footer-band"></div>
  <div class="site-pill">
    <svg width="22" height="22" viewBox="0 0 22 22" aria-hidden="true">
      <g fill="none" stroke="#fff" stroke-width="2"><circle cx="11" cy="11" r="9"/><ellipse cx="11" cy="11" rx="4" ry="9"/><path d="M2 11h18"/></g>
    </svg>
    <span>www.quavi.com</span>
  </div>
</main>
</body>
</html>
```